Packaging for Hair Fibers Product

We are a start up company looking for a new packaging design for hair building fibers. These are aimed at predominantly men but also women as well. We already have a logo and i have the packaging design from our competitors. We are wanting to keep the look masculine as 90% of our users will be middle aged men. We would like the colours to be black and white but are open to other colours as well.
It will need to have our logo and the following somewhere on the front.
"Instant Fuller & Thicker Hair" & "Natural Hair Building Fibers" "28g" or "Net Weight 28g"
We only need the front of the packaging designed, please make the other sides of the packaging the same colour but blank.
Target Market(s)
Men 25+
Industry/Entity Type
Hair And Beauty
Requirements
Must have
- Logo which i have included. and the following somewhere on the front.
- "Instant Fuller & Thicker Hair" ; "Natural Hair Building Fibers" "28g" or "Net Weight 28g"
Nice to have
- Make it stand out from the competition or similar to the tarsick example.

```html
<!DOCTYPE html>
<html lang="en">
<head>
<meta charset="utf-8">
<title>Fibrane Pro – Hair Building Fibers Packaging Fronts</title>
<link rel="stylesheet" href="https://fonts.googleapis.com/css2?family=Montserrat:wght@400;500;700&family=Roboto+Condensed:wght@400;500&display=swap">
<style>
  :root {
    --page: #ffffff;
    --box: #050505;
    --strand: #1b1b1b;
    --ink: #ffffff;
    --accent-her: #e8197d;
  }
  * { box-sizing: border-box; margin: 0; padding: 0; }
  html, body { width: 1200px; height: 1200px; overflow: hidden; background: var(--page); }
  body { font-family: "Montserrat", Arial, sans-serif; color: var(--ink); }

  .board {
    width: 1200px; height: 1200px;
    display: flex; justify-content: center; align-items: center; gap: 44px;
  }

  .pack-front {
    position: relative;
    width: 244px; height: 630px;
    background: var(--box);
    overflow: hidden;
  }
  .strand-field {
    position: absolute; left: 0; right: 0; top: 190px; bottom: 60px;
    background:
      radial-gradient(ellipse 70% 30% at 50% 8%, var(--strand), transparent 70%),
      radial-gradient(ellipse 40% 60% at 50% 50%, #111 0%, transparent 75%);
  }

  .brand { position: absolute; left: 24px; right: 20px; }
  .brand-name {
    font-weight: 500; font-size: 30px; letter-spacing: 4px; line-height: 1;
    white-space: nowrap;
  }
  .brand-sub {
    font-size: 10px; letter-spacing: 3px; text-align: right; margin-top: 2px;
  }
  .tagline-small {
    font-weight: 700; font-size: 10px; letter-spacing: 0.2px; white-space: nowrap;
  }
  .brand-mark {
    width: 56px; height: 56px;
    border: 2px solid var(--ink);
    margin: 0 auto 18px;
  }

  .claim {
    position: absolute; left: 24px; right: 20px;
    font-weight: 700; font-size: 19px; line-height: 27px; text-transform: uppercase;
  }
  .weight {
    position: absolute; left: 24px;
    font-weight: 700; font-size: 15px; line-height: 20px; text-transform: uppercase;
  }

  /* Variant 1: classic */
  .v-classic .brand { top: 76px; }
  .v-classic .tagline-small { margin-top: 12px; }
  .v-classic .claim { top: 372px; }
  .v-classic .weight { top: 555px; }

  /* Variant 2: spaced with mark */
  .v-spaced .brand { top: 36px; left: 22px; right: 22px; text-align: center; }
  .v-spaced .brand-name {
    font-family: "Roboto Condensed", "Arial Narrow", sans-serif;
    font-weight: 400; font-size: 21px; letter-spacing: 6px; margin-right: -6px;
  }
  .v-spaced .tagline-small { font-weight: 400; font-size: 9.5px; margin-top: 8px; }
  .v-spaced .claim { top: 370px; }
  .v-spaced .weight { top: 552px; }

  /* Variant 3: for her */
  .v-her .brand { top: 70px; left: 16px; right: 16px; text-align: center; }
  .v-her .tagline-small { color: var(--accent-her); font-weight: 400; }
  .v-her .brand-name { font-weight: 400; font-size: 24px; letter-spacing: 2px; margin-top: 2px; }
  .v-her .brand-sub { text-align: center; }
  .v-her .claim { top: 325px; left: 10px; right: 10px; color: var(--accent-her); text-align: center; font-size: 21px; line-height: 33px; letter-spacing: -0.5px; }
  .v-her .weight { top: 545px; left: 0; right: 0; text-align: center; font-weight: 400; font-size: 14px; }

  /* Variant 4: for him */
  .v-him .brand { top: 88px; }
  .v-him .tagline-small { font-weight: 400; }
  .v-him .brand-name { font-weight: 400; font-size: 21px; letter-spacing: 4px; margin-top: 4px; }
  .v-him .claim { top: 355px; }
  .v-him .weight { top: 530px; }
</style>
</head>
<body>
<main class="board">

  <section class="pack-front v-classic">
    <div class="strand-field" role="img" aria-label="Faint interwoven hair strand pattern"></div>
    <div class="brand">
      <div class="brand-name">FIBRANE</div>
      <div class="brand-sub">PRO</div>
      <div class="tagline-small">NATURAL HAIR BUILDING FIBERS</div>
    </div>
    <p class="claim">Instant Fuller<br>&amp;<br>Thicker Hair</p>
    <p class="weight">Net Weight<br>28G</p>
  </section>

  <section class="pack-front v-spaced">
    <div class="strand-field" role="img" aria-label="Faint interwoven hair strand pattern"></div>
    <div class="brand">
      <div class="brand-mark"></div>
      <div class="brand-name">FIBRANE PRO</div>
      <div class="tagline-small">NATURAL HAIR BUILDING FIBERS</div>
    </div>
    <p class="claim">Instant Fuller<br>&amp;<br>Thicker Hair</p>
    <p class="weight">Net Weight<br>28G</p>
  </section>

  <section class="pack-front v-her">
    <div class="strand-field" role="img" aria-label="Faint interwoven hair strand pattern"></div>
    <div class="brand">
      <div class="tagline-small">NATURAL HAIR BUILDING FIBERS</div>
      <div class="brand-name">FIBRANEPRO</div>
      <div class="brand-sub">FOR HER</div>
    </div>
    <p class="claim">Instant Fuller<br>&amp;<br>Thicker Hair</p>
    <p class="weight">Net Weight 28G</p>
  </section>

  <section class="pack-front v-him">
    <div class="strand-field" role="img" aria-label="Faint interwoven hair strand pattern"></div>
    <div class="brand">
      <div class="tagline-small">NATURAL HAIR BUILDING FIBERS</div>
      <div class="brand-name">FIBRANEPRO</div>
      <div class="brand-sub">FOR HIM</div>
    </div>
    <p class="claim">Instant Fuller<br>&amp;<br>Thicker Hair</p>
    <p class="weight">Net Weight<br>28G</p>
  </section>

</main>
</body>
</html>
```